One Page Website for Personal Trainer in London

I have a logo and need a one page website designed around my branding. I am a freelance Personal Trainer based in London specialising in bodyweight training for men and women. I would like the site to be modern and clean but not overtly urban in design.
I need the following headings:
About Me
My Services
Events
Blog
I don't need them to be seperate pages but if they can link to further down the page that would be great.
Industry/Entity Type
Personal Trainer
Coding
Coded - Design and coding required
Number of Pages Required
1 page
Requirements
Must have
- I need the following headings:
- About Me
- My Services
- Events
- Blog
- mobile friendly formatting
- health and fitness related photography
- Colour scheme in keeping with my existing logo

```html
<!DOCTYPE html>
<html lang="en">
<head>
<meta charset="utf-8">
<title>Harriet Vale Personal Training</title>
<link href="https://fonts.googleapis.com/css2?family=Poppins:wght@300;400;500;600;700&display=swap" rel="stylesheet">
<style>
:root{
  --orange:#f07c1b;
  --orange-dark:#d9650b;
  --black:#111111;
  --ink:#222222;
  --grey:#666666;
  --light:#eeeeee;
  --white:#ffffff;
}
*{box-sizing:border-box;margin:0;padding:0}
html,body{width:1200px;height:4353px;overflow:hidden}
body{font-family:'Poppins',sans-serif;color:var(--ink);background:var(--white);position:relative}
section,header,footer{position:absolute;left:0;width:1200px;overflow:hidden}
.abs{position:absolute}
.photo{position:absolute}
.section-title{position:absolute;left:0;width:100%;text-align:center;font-weight:700;font-size:36px;letter-spacing:.5px}
.title-rule{position:absolute;width:90px;height:3px;background:var(--orange);left:555px}
.btn-outline{position:absolute;border:2px solid var(--white);color:var(--white);font-size:13px;font-weight:600;text-align:center;letter-spacing:.5px}
.btn-solid{position:absolute;background:var(--orange);color:var(--white);font-size:14px;font-weight:600;text-align:center;letter-spacing:.5px}

/* Hero */
.hero{top:0;height:630px;background:#1a1a1a}
.hero .photo{left:0;top:0;width:1200px;height:630px;background:linear-gradient(100deg,#0d0d0d 0%,#262626 40%,#5a5a5a 62%,#2a2a2a 80%,#0d0d0d 100%)}
.brand{position:absolute;left:138px;top:28px;display:flex;align-items:center;gap:10px}
.brand-mark{width:40px;height:40px;border-radius:50%;background:var(--orange)}
.brand-name{font-weight:600;font-size:22px;color:var(--orange);line-height:1.1}
.brand-sub{display:block;font-size:11px;letter-spacing:2px}
.main-nav{position:absolute;left:468px;top:44px;display:flex;gap:26px;font-size:15px;color:var(--white)}
.main-nav a{color:var(--white);text-decoration:none}
.main-nav a.active{border-bottom:2px solid var(--orange);padding-bottom:4px}
.social{position:absolute;display:flex;gap:12px}
.social span{width:13px;height:13px;border-radius:50%;background:var(--white)}
.hero .kicker{position:absolute;left:197px;top:232px;border:2px solid var(--white);color:var(--white);font-weight:700;font-size:24px;padding:4px 12px}
.hero h1{position:absolute;left:197px;top:290px;color:var(--white);font-weight:700;font-size:56px;letter-spacing:.5px}
.hero .btn-solid{left:197px;top:365px;width:150px;height:44px;line-height:44px}
.dots{position:absolute;left:584px;top:590px;display:flex;gap:8px}
.dots span{width:7px;height:7px;border-radius:50%;background:var(--white)}
.dots span:first-child{background:var(--orange)}
.hero-tab{position:absolute;left:580px;top:608px;width:40px;height:22px;background:var(--orange)}
.chat-tab{position:absolute;left:1002px;top:606px;width:180px;height:24px;background:#333;color:#ccc;font-size:11px;line-height:24px;padding-left:26px}
.chat-tab::before{content:"";position:absolute;left:9px;top:7px;width:10px;height:10px;border-radius:50%;background:var(--orange)}

/* Audience */
.audience{top:630px;height:362px;background:var(--orange)}
.audience .photo{left:505px;top:50px;width:190px;height:312px;background:linear-gradient(180deg,#c4651a,#7a3e10)}
.audience h2{position:absolute;color:var(--white);font-weight:700;font-size:36px;top:92px}
.audience p{position:absolute;color:var(--white);font-size:13px;line-height:18px;width:300px;top:140px}
.audience .men h2,.audience .men p{right:720px;text-align:right}
.audience .women h2,.audience .women p{left:755px}
.audience .btn-outline{top:240px;width:110px;height:36px;line-height:32px}
.audience .men .btn-outline{left:348px}
.audience .women .btn-outline{left:758px}

/* About */
.about{top:992px;height:483px;background:var(--white)}
.about .photo{left:0;top:150px;width:1200px;height:333px;background:linear-gradient(180deg,#ffffff 0%,#ececec 60%,#dcdcdc 100%)}
.about .section-title{top:55px;color:var(--ink)}
.about .title-rule{top:108px}
.about p{position:absolute;top:155px;width:300px;font-size:13px;line-height:20px;color:#555}
.about .col-left{left:290px;text-align:right}
.about .col-right{left:620px}
.about .btn-outline{left:530px;top:365px;width:140px;height:38px;line-height:34px;border-color:var(--orange);color:var(--orange)}

/* Services */
.services{top:1475px;height:600px;background:var(--black);color:var(--white)}
.services .section-title{top:75px;color:var(--white)}
.services .title-rule{top:128px}
.services .intro{position:absolute;left:300px;width:600px;top:150px;text-align:center;font-size:14px;line-height:22px}
.service{position:absolute;width:420px;display:flex;gap:22px;align-items:flex-start}
.service h3{font-size:14px;font-weight:700;margin-bottom:4px}
.service p{font-size:13px;line-height:20px;color:#ddd}
.service.left{left:160px;flex-direction:row;text-align:right;justify-content:flex-end}
.service.right{left:625px}
.service .icon{flex:none;width:52px;height:52px;background:var(--orange);display:flex;align-items:center;justify-content:center}
.service h3.light{font-weight:400}

/* Events */
.events{top:2075px;height:667px;background:#f2f2f2}
.events .photo{left:0;top:0;width:1200px;height:667px;background:linear-gradient(90deg,#9a9a9a 0%,#c9c9c9 30%,#ebebeb 55%,#f5f5f5 100%)}
.events h2{position:absolute;left:585px;top:70px;font-weight:700;font-size:38px;color:var(--ink)}
.events .title-rule{left:728px;top:130px}
.calendar{position:absolute;left:465px;top:160px;width:615px;background:#dcdcdc}
.cal-head{height:48px;background:var(--orange);color:var(--white);font-weight:700;font-size:17px;line-height:48px;padding-left:20px;display:flex;align-items:center;gap:8px}
.cal-head .arrow{width:18px;height:18px;background:var(--white);display:inline-block}
.cal-strip{height:22px;background:#1a1a1a}
.cal-table{width:100%;border-collapse:separate;border-spacing:4px;font-size:14px;text-align:center}
.cal-table th{background:var(--orange);color:var(--white);font-size:12px;font-weight:600;height:24px}
.cal-table td{background:#f2f2f2;height:42px;color:#333;position:relative}
.cal-table td.event{color:var(--orange)}
.cal-table td.event::after{content:"";position:absolute;left:50%;bottom:6px;width:4px;height:4px;margin-left:-2px;border-radius:50%;background:var(--orange)}
.cal-table td.today{background:var(--orange);color:var(--white)}
.cal-table td.blank{background:transparent}
.cal-foot{height:44px;background:var(--black);color:var(--white);font-weight:700;font-size:15px;display:flex;align-items:center;gap:10px}
.cal-foot .day{width:36px;height:44px;background:var(--orange);text-align:center;line-height:44px}

/* Call to action */
.cta{top:2742px;height:378px;background:var(--orange)}
.cta .photo{left:0;top:0;width:1200px;height:378px;background:linear-gradient(180deg,#e8832e,#f07c1b 50%,#d46a14)}
.cta .small{position:absolute;width:100%;top:130px;text-align:center;color:var(--white);font-size:20px;letter-spacing:1px}
.cta h2{position:absolute;width:100%;top:158px;text-align:center;color:var(--white);font-weight:700;font-size:44px}
.cta .btn-outline{left:530px;top:230px;width:140px;height:40px;line-height:36px}

/* Blog */
.blog{top:3120px;height:625px;background:var(--white)}
.blog h2{position:absolute;left:155px;top:85px;font-weight:700;font-size:36px}
.blog .pager{position:absolute;top:93px;display:flex;gap:6px;left:970px}
.blog .pager span{width:26px;height:26px;border:2px solid #999;display:flex;align-items:center;justify-content:center}
.blog .pager span.next{border-color:var(--orange)}
.post{position:absolute;top:160px;width:275px}
.post .thumb{height:158px;background:linear-gradient(135deg,#d8d8d8,#b9b9b9)}
.post.featured .thumb{border:6px solid var(--orange)}
.post h3{font-size:17px;font-weight:700;line-height:23px;margin-top:26px}
.post p{font-size:13px;line-height:23px;color:#444;margin-top:10px}
.blog .btn-solid{left:532px;top:505px;width:135px;height:44px;line-height:44px}

/* Contact */
.contact{top:3745px;height:608px;background:var(--black);color:var(--white)}
.contact .section-title{top:65px;color:var(--white)}
.contact .title-rule{top:115px}
.field{position:absolute;border:2px solid #cfcfcf;height:40px;font-size:14px;color:var(--white);padding:6px 10px}
.contact .info{position:absolute;left:195px;font-size:13px;display:flex;align-items:center;gap:10px}
.contact .btn-solid{left:868px;top:397px;width:137px;height:46px;line-height:46px}
.footer-rule{position:absolute;left:195px;top:492px;width:810px;height:2px;background:#555}
.copyright{position:absolute;left:0;width:100%;top:520px;text-align:center;font-size:14px}
</style>
</head>
<body>

<header class="hero" id="home">
  <div class="photo" role="img" aria-label="Black and white photo of a female athlete sprinting in a dark gym"></div>
  <div class="brand">
    <span class="brand-mark"></span>
    <span class="brand-name">Harriet Vale<span class="brand-sub">PERSONAL TRAINING</span></span>
  </div>
  <nav class="main-nav">
    <a class="active" href="#home">Home</a>
    <a href="#about">About Me</a>
    <a href="#services">My Services</a>
    <a href="#events">Events</a>
    <a href="#blog">Blog</a>
    <a href="#contact">Contact Me</a>
  </nav>
  <div class="social" style="left:1015px;top:48px"><span></span><span></span><span></span><span></span></div>
  <div class="kicker">GET IN TO SHAPE</div>
  <h1>AND BE HAPPY</h1>
  <div class="btn-solid">LEARN MORE</div>
  <div class="dots"><span></span><span></span><span></span></div>
  <div class="hero-tab">
    <svg width="40" height="22" viewBox="0 0 40 22"><path d="M15 8 L20 13 L25 8" stroke="#fff" stroke-width="2" fill="none"/></svg>
  </div>
  <div class="chat-tab">Online - Leave a message</div>
</header>

<section class="audience">
  <div class="photo" role="img" aria-label="Photo of a male and a female trainer standing side by side"></div>
  <div class="men">
    <h2>FOR MEN</h2>
    <p>Lorem ipsum dolor sit amet, conse ctetur adipiscing elit. Suspendisse pulvinar, velit nec pharetra interdum, ante tellus ornare mi, et mollis tellus neque vitae elit.</p>
    <div class="btn-outline">GET STARTED</div>
  </div>
  <div class="women">
    <h2>FOR WOMEN</h2>
    <p>Lorem ipsum dolor sit amet, conse ctetur adipiscing elit. Suspendisse pulvinar, velit nec pharetra interdum, ante tellus ornare mi, et mollis tellus neque vitae elit.</p>
    <div class="btn-outline">GET STARTED</div>
  </div>
</section>

<section class="about" id="about">
  <div class="photo" role="img" aria-label="Faded photo of a gym floor with training equipment"></div>
  <h2 class="section-title">ABOUT ME</h2>
  <div class="title-rule"></div>
  <p class="col-left">Lorem ipsum dolor sit amet, consectetur adipiscing elit. Curabitur sed purus quam. Vestibulum lobortis consequat mauris id fringilla. Morbi eros purus, commodo non tortor ut, tempus ornare ant. Suspendisse suscipit nec metus non pellentesque. Morbi at enim nisl. Phasellus sed condimentum enim, non viverra eros.</p>
  <p class="col-right">Quisque commodo erat vel sapien suscipit accumsan. Fusce eu eleifend mi. Integer hendrerit, dolor non sagittis consequat, enim ex gravida lacus, quis dignissim augue urna non mauris. Nullam eros massa, fringilla sit amet leo quis, tincidunt lobortis leo. Praesent imperdiet sapien dapibus, hendrerit nisi ac, aliquet diam.</p>
  <div class="btn-outline">CONTACT ME</div>
</section>

<section class="services" id="services">
  <h2 class="section-title">MY SERVICES</h2>
  <div class="title-rule"></div>
  <p class="intro">Lorem ipsum dolor sit amet, consectetur adipiscing elit. Curabitur sed purus quam. Vestibulum lobortis consequat mauris id fringilla. Morbi eros purus, commodo non.</p>

  <div class="service left" style="top:250px">
    <div><h3>WEIGHT LOSS</h3><p>Lorem ipsum dolor sit amet, consectetur<br>adipiscing elit. Curabitur sed purus.</p></div>
    <div class="icon"><svg width="30" height="30" viewBox="0 0 30 30" fill="none" stroke="#fff" stroke-width="2.5"><rect x="5" y="10" width="20" height="15"/><path d="M10 10 V6 H20 V10 M15 14 V19"/></svg></div>
  </div>
  <div class="service right" style="top:250px">
    <div class="icon"><svg width="30" height="30" viewBox="0 0 30 30" fill="#fff"><circle cx="10" cy="7" r="3"/><path d="M6 13 H18 L24 9 L25 12 L18 16 V26 H14 V18 H8 Z"/></svg></div>
    <div><h3>BODY BUILDING</h3><p>Lorem ipsum dolor sit amet, consectetur<br>adipiscing elit. Curabitur sed purus.</p></div>
  </div>

  <div class="service left" style="top:340px">
    <div><h3>WEIGHT LIFTING</h3><p>Lorem ipsum dolor sit amet, consectetur<br>adipiscing elit. Curabitur sed purus.</p></div>
    <div class="icon"><svg width="32" height="20" viewBox="0 0 32 20" fill="#fff"><rect x="2" y="5" width="4" height="10"/><rect x="6" y="2" width="4" height="16"/><rect x="10" y="8" width="12" height="4"/><rect x="22" y="2" width="4" height="16"/><rect x="26" y="5" width="4" height="10"/></svg></div>
  </div>
  <div class="service right" style="top:340px">
    <div class="icon"><svg width="30" height="30" viewBox="0 0 30 30" fill="none" stroke="#fff" stroke-width="2.5"><circle cx="8" cy="22" r="5"/><circle cx="23" cy="22" r="5"/><path d="M8 22 L14 12 L23 22 M12 9 H17"/></svg></div>
    <div><h3>INDOOR CYCLING</h3><p>Lorem ipsum dolor sit amet, consectetur<br>adipiscing elit. Curabitur sed purus.</p></div>
  </div>

  <div class="service left" style="top:430px">
    <div><h3>BOXING FOR GIRLS</h3><p>Lorem ipsum dolor sit amet, consectetur<br>adipiscing elit. Curabitur sed purus.</p></div>
    <div class="icon"><svg width="30" height="30" viewBox="0 0 30 30" fill="#fff"><circle cx="15" cy="6" r="3"/><path d="M10 11 H20 L22 18 H19 L18 14 V27 H15.5 V20 H14.5 V27 H12 V14 L11 18 H8 Z"/></svg></div>
  </div>
  <div class="service right" style="top:430px">
    <div class="icon"><svg width="30" height="30" viewBox="0 0 30 30" fill="#fff"><circle cx="20" cy="6" r="3"/><path d="M17 10 L8 14 L9 16 L15 14 L12 22 L5 25 L6 27 L14 24 L17 18 L21 22 L22 28 H24 L23 20 L19 15 L21 12 L26 14 L27 12 Z"/></svg></div>
    <div><h3 class="light">PSYCHOLOGY TRAINING</h3><p>Lorem ipsum dolor sit amet, consectetur<br>adipiscing elit. Curabitur sed purus.</p></div>
  </div>
</section>

<section class="events" id="events">
  <div class="photo" role="img" aria-label="Photo of a man doing a one-arm push-up in a bright gym"></div>
  <h2>MY EVENT CALENDAR</h2>
  <div class="title-rule"></div>
  <div class="calendar">
    <div class="cal-head">OCTOBER, 2017 <span class="arrow"></span><span class="arrow"></span></div>
    <div class="cal-strip"></div>
    <table class="cal-table">
      <tr><th>MON</th><th>TUE</th><th>WED</th><th>THU</th><th>FRI</th><th>SAT</th><th>SUN</th></tr>
      <tr><td>-</td><td>-</td><td>-</td><td>-</td><td>-</td><td>-</td><td class="event">1</td></tr>
      <tr><td>2</td><td class="event">3</td><td>4</td><td>5</td><td class="event">6</td><td class="event">7</td><td class="event">8</td></tr>
      <tr><td>9</td><td class="event">10</td><td>11</td><td>12</td><td class="event">13</td><td class="event">14</td><td class="event">15</td></tr>
      <tr><td>16</td><td class="event">17</td><td>18</td><td>19</td><td class="today">20</td><td class="event">21</td><td class="event">22</td></tr>
      <tr><td>23</td><td class="event">24</td><td>25</td><td>26</td><td class="event">27</td><td class="event">28</td><td class="event">29</td></tr>
      <tr><td>30</td><td class="event">31</td><td class="blank"></td><td class="blank"></td><td class="blank"></td><td class="blank"></td><td class="blank"></td></tr>
    </table>
    <div class="cal-foot"><span class="day">20</span>WEIGHT LOSS</div>
  </div>
</section>

<section class="cta">
  <div class="photo" role="img" aria-label="Orange-tinted photo of a smiling group fitness class"></div>
  <div class="small">START YOUR</div>
  <h2>TRAINING TODAY</h2>
  <div class="btn-outline">CONTACT ME</div>
</section>

<section class="blog" id="blog">
  <h2>LATEST BLOG</h2>
  <div class="pager">
    <span><svg width="10" height="10" viewBox="0 0 10 10"><path d="M7 1 L3 5 L7 9" stroke="#999" stroke-width="2" fill="none"/></svg></span>
    <span class="next"><svg width="10" height="10" viewBox="0 0 10 10"><path d="M3 1 L7 5 L3 9" stroke="#f07c1b" stroke-width="2" fill="none"/></svg></span>
  </div>
  <article class="post" style="left:155px">
    <div class="thumb" role="img" aria-label="Photo of a woman lifting dumbbells"></div>
    <h3>Lorem ipsum dolor sit amet, consectetur adipiscing.</h3>
    <p>Vestibulum lobortis consequat mauris id fringilla. Morbi eros purus, commodo non tortor ut, tempus ornare..</p>
  </article>
  <article class="post featured" style="left:463px">
    <div class="thumb" role="img" aria-label="Photo of a woman training on gym machines"></div>
    <h3>Lorem ipsum dolor sit amet, consectetur adipiscing.</h3>
    <p>Vestibulum lobortis consequat mauris id fringilla. Morbi eros purus, commodo non tortor ut, tempus ornare..</p>
  </article>
  <article class="post" style="left:773px">
    <div class="thumb" role="img" aria-label="Photo of an aerobics class on steps"></div>
    <h3>Lorem ipsum dolor sit amet, consectetur adipiscing.</h3>
    <p>Vestibulum lobortis consequat mauris id fringilla. Morbi eros purus, commodo non tortor ut, tempus ornare..</p>
  </article>
  <div class="btn-solid">Read All &#9662;</div>
</section>

<footer class="contact" id="contact">
  <h2 class="section-title">CONTACT ME</h2>
  <div class="title-rule"></div>
  <div class="field" style="left:195px;top:160px;width:390px">Name</div>
  <div class="field" style="left:615px;top:160px;width:390px">Email</div>
  <div class="field" style="left:195px;top:212px;width:390px">Phone No.</div>
  <div class="field" style="left:615px;top:212px;width:390px">Subject</div>
  <div class="field" style="left:195px;top:264px;width:810px;height:118px">Message</div>
  <div class="info" style="top:403px">
    <svg width="14" height="14" viewBox="0 0 14 14" fill="#fff"><path d="M3 1 L5 1 L6 4 L4.5 5.5 C5.5 7.5 6.5 8.5 8.5 9.5 L10 8 L13 9 L13 11 C13 12 12 13 11 13 C5.5 13 1 8.5 1 3 C1 2 2 1 3 1 Z"/></svg>
    <strong>(020) 555-0148</strong>
  </div>
  <div class="info" style="top:430px">
    <svg width="14" height="12" viewBox="0 0 14 12" fill="none" stroke="#fff" stroke-width="1.5"><rect x="1" y="1" width="12" height="10"/><path d="M1 1 L7 6 L13 1"/></svg>
    info@harrietvalept.com
  </div>
  <div class="btn-solid">SUBMIT &#9662;</div>
  <div class="footer-rule"></div>
  <div class="copyright">© Copyright 2017, Harriet Vale Personal Training. All rights reserved.</div>
  <div class="social" style="left:955px;top:523px"><span></span><span style="background:var(--orange)"></span><span></span><span></span></div>
</footer>

</body>
</html>
```